The Ledger Beneath Offerings Book Cover

I need a book cover design for a book titled "The Ledger Beneath Offerings". The sub title IS "Where the Collection Plate Quietly Goes". The Author's name is: Kwabena Lucas Adebanjo

I want a creative book cover that's exciting, unique and stand outs.

What the book is about – the book exposes “tithing”. Tithing is taught by many Church Pastors as the process of an individual paying the church/Pastors 10% of all income received. A lot of greedy Pastors teach tithes for the purpose of receiving money from their members so as to enrich themselves and fund their lavish lifestyles e.g. private jets and luxury cars.

Target Market(s)

Christians / Religious

Font styles to use
Serif

Requirements
Must have
• Book Title
• Author's name
Nice to have
• some graphical representation reflecting what the book is about
Should not have
• Not applicable

```html
<!DOCTYPE html>
<html lang="en">
<head>
<meta charset="utf-8">
<title>The Ledger Beneath Offerings — Book Cover</title>
<link rel="stylesheet" href="https://fonts.googleapis.com/css2?family=Libre+Baskerville:wght@700&family=Open+Sans:wght@400&display=swap">
<style>
  :root {
    --backdrop: #2f4f94;
    --cover-black: #1d1d1d;
    --cover-black-deep: #121212;
    --accent-orange: #f4a22c;
    --title-white: #eeeeea;
    --text-white: #f4f4f4;
    --photo-dark: #120d08;
    --photo-wood: #3a2716;
    --photo-brass: #9a8247;
    --photo-brass-light: #c9b070;
    --photo-skin: #a88a74;
    --photo-sleeve: #0c0c0c;
  }
  html, body {
    margin: 0;
    padding: 0;
    width: 1200px;
    height: 768px;
    overflow: hidden;
    background: var(--backdrop);
  }
  .stage {
    position: relative;
    width: 1200px;
    height: 768px;
  }
  .book-cover {
    position: absolute;
    left: 417px;
    top: 77px;
    width: 366px;
    height: 540px;
    background: linear-gradient(180deg, var(--cover-black) 0%, var(--cover-black-deep) 100%);
    overflow: hidden;
  }
  .title-line {
    position: absolute;
    left: 0;
    right: 0;
    margin: 0;
    color: var(--title-white);
    font-family: "Libre Baskerville", "Times New Roman", serif;
    font-weight: 700;
    text-align: center;
    line-height: 1;
    white-space: nowrap;
  }
  .title-the {
    top: 36px;
    font-size: 44px;
    letter-spacing: 3px;
  }
  .title-main {
    top: 78px;
    font-size: 57px;
    letter-spacing: 2px;
  }
  .title-tail {
    top: 137px;
    font-size: 19px;
    letter-spacing: 1.5px;
  }
  .accent-band {
    position: absolute;
    top: 197px;
    left: 0;
    right: 0;
    height: 6px;
    background: var(--accent-orange);
  }
  .cover-photo {
    position: absolute;
    top: 203px;
    left: 0;
    right: 0;
    bottom: 0;
    background:
      radial-gradient(ellipse 30% 32% at 55% 58%, var(--photo-brass-light) 0%, rgba(201, 176, 112, 0) 100%),
      radial-gradient(ellipse 42% 48% at 55% 60%, var(--photo-brass) 0%, rgba(154, 130, 71, 0) 100%),
      radial-gradient(ellipse 38% 16% at 16% 22%, var(--photo-skin) 0%, rgba(168, 138, 116, 0) 100%),
      radial-gradient(ellipse 18% 40% at 92% 50%, var(--photo-sleeve) 0%, rgba(12, 12, 12, 0) 100%),
      linear-gradient(90deg, var(--photo-wood) 0%, rgba(58, 39, 22, 0.4) 40%, rgba(20, 14, 9, 0.6) 100%),
      linear-gradient(180deg, #2a1e14 0%, var(--photo-dark) 100%);
  }
  .photo-fade {
    position: absolute;
    left: 0;
    right: 0;
    bottom: 0;
    height: 90px;
    background: linear-gradient(180deg, rgba(18, 13, 8, 0) 0%, rgba(12, 10, 8, 0.9) 100%);
  }
  .subtitle {
    position: absolute;
    top: 228px;
    left: 0;
    right: 0;
    margin: 0;
    color: var(--text-white);
    font-family: "Open Sans", Arial, sans-serif;
    font-weight: 400;
    font-size: 16px;
    line-height: 22px;
    letter-spacing: 0.3px;
    text-align: center;
    text-transform: uppercase;
  }
  .author {
    position: absolute;
    top: 497px;
    left: 0;
    right: 0;
    margin: 0;
    color: var(--text-white);
    font-family: "Open Sans", Arial, sans-serif;
    font-weight: 400;
    font-size: 14px;
    line-height: 18px;
    letter-spacing: 1.5px;
    text-align: center;
    text-transform: uppercase;
  }
</style>
</head>
<body>
  <main class="stage">
    <article class="book-cover">
      <div class="cover-photo" role="img" aria-label="Photo of a hand dropping a coin into a brass offering box held in another hand"></div>
      <div class="photo-fade"></div>
      <h1 class="title-line title-the">THE</h1>
      <p class="title-line title-main">LEDGER</p>
      <p class="title-line title-tail">BENEATH OFFERINGS</p>
      <div class="accent-band"></div>
      <p class="subtitle">Where the Collection Plate<br>Quietly Goes</p>
      <p class="author">Kwabena Lucas Adebanjo</p>
    </article>
  </main>
</body>
</html>
```